Lumen Keyvault Password Manager WebApp Design

Lumen Keyvault is seeking an expert UI designer to provide a fresh and modern visual appeal for our product. Our inspiration comes from two major tools that have successfully managed to balance functionality and design aesthetics - Orbix Folder and Vaultmint. We want our application to exude a similar trustworthiness and modernity, through a clean, intuitive and responsive design.
We have established preliminary mockups and would like the designer to work within these parameters while enhancing the overall user experience. The primary tasks will involve innovative and improved designs of the login screen and the password screen, both being crucial touchpoints for our users. The login screen also serves a crucial role in demonstrating how our system works.
Key Elements:
Logo Integration: We are providing the logo for Lumen Keyvault. The design should align with the logo, both in terms of colors and overall aesthetic, to ensure a cohesive brand identity.
Color Palette: The UI design should adhere to the color palette derived from the logo to maintain brand consistency. The design should effectively utilize these colors to highlight important elements and improve user engagement.
Trustworthy and Modern Design: The UI should be professional and trustworthy. It should mirror the look and feel of Orbix Folder's simplicity and Vaultmint's solid security design, which inspires user confidence.
Adherence to Mockup Boundaries: The existing mockups serve as a guideline for the layout and placement of elements. The design should respect these boundaries while bringing innovation and visual appeal.
Improved Login Screen: The login screen is a key part of the user's journey and should be designed with utmost care. It should be intuitive, easy-to-use, visually engaging, and educative, showcasing how the system operates and encouraging users to sign in with confidence.
Enhanced Password Screen: The password screen, another key user touchpoint, needs improvement. The different types of passwords should be made more visible and intuitive, easing user interaction and enhancing the overall experience.
Prospective designers are encouraged to test our current version available for free at app.lumenkeyvault.com to understand the product better and contribute to meaningful design enhancements.
The goal of this project is to provide a visually compelling and user-friendly interface for Lumen Keyvault that inspires user trust, while adhering to the branding elements, including color scheme and logo design. The ideal designer will have a proven track record of creating compelling UI designs that enhance user experience and engagement.
We preferred the design to be in Figma.
Please provide the 3 design so we can evaluate if we like to choice you:
1. Login Page.
2. Passwords View design
3. Single Passwod Page
We need all the pages to be design that are provided as screenshots.

```html
<!DOCTYPE html>
<html lang="en">
<head>
<meta charset="utf-8">
<title>Lumen Keyvault – Sign in and Vault</title>
<link href="https://fonts.googleapis.com/css2?family=Roboto:wght@300;400;500;700&display=swap" rel="stylesheet">
<style>
:root{
  --canvas:#dcdcdc;
  --white:#ffffff;
  --paper:#f8f7f5;
  --panel:#f7f8fd;
  --blue:#3d6fc9;
  --blue-soft:#e9eef8;
  --link:#2b67e0;
  --ink:#2a2a2a;
  --ink-soft:#3b3f4a;
  --grey:#777;
  --line:#ececec;
  --red:#e5533d;
}
*{box-sizing:border-box;margin:0;padding:0}
html,body{width:779px;height:1200px;overflow:hidden}
body{background:var(--canvas);font-family:'Roboto',sans-serif;color:var(--ink);position:relative}
.abs{position:absolute}

/* ---------- shared ---------- */
.screen{position:absolute;left:50px;width:678px;background:var(--paper);box-shadow:0 2px 8px rgba(0,0,0,.08);overflow:hidden}
.topbar{position:absolute;left:0;top:0;width:100%;height:42px;background:var(--white)}
.brand{position:absolute;left:14px;top:13px;display:flex;align-items:center;gap:6px;font-size:12px;font-weight:300;color:#555;letter-spacing:.1px}
.brand-mark{width:12px;height:12px;background:var(--blue);border-radius:2px}

/* ---------- sign-in screen ---------- */
.signin{top:57px;height:496px}
.welcome{position:absolute;left:0;width:100%;top:62px;line-height:22px;text-align:center;color:var(--blue);font-weight:700;font-size:17px}
.intro{position:absolute;left:0;width:100%;top:87px;text-align:center;font-size:14px;line-height:18px;color:var(--ink-soft)}
.info-card{position:absolute;top:149px;width:266px;height:188px;background:var(--white);border-radius:10px;box-shadow:0 4px 12px rgba(0,0,0,.06);text-align:center}
.info-card.files{left:63px}
.info-card.drive{left:350px}
.info-icon{position:absolute;left:98px;top:16px;width:70px;height:70px;border-radius:50%;background:var(--blue-soft)}
.info-icon svg{position:absolute;left:17px;top:15px}
.info-text{position:absolute;left:4px;right:4px;top:90px;font-size:13.6px;line-height:20.7px;color:var(--ink)}
.pager{position:absolute;left:634px;top:217px;display:flex;flex-direction:column;gap:10.5px}
.pager span{width:10px;height:10px;border-radius:50%;background:#6f93d8}
.pager span.on{background:var(--white);border:2px solid #6f93d8;box-shadow:inset 0 0 0 1.5px #fff,inset 0 0 0 4px #6f93d8}
.account{position:absolute;left:145px;top:366px;width:389px;height:52px;background:var(--white);border:1px solid #ececec;border-radius:4px}
.avatar{position:absolute;left:34px;top:10px;width:32px;height:32px;border-radius:50%;background:var(--red);color:#fff;font-weight:500;font-size:17px;line-height:32px;text-align:center}
.account-name{position:absolute;left:82px;top:7px;font-size:13.5px;color:var(--ink-soft)}
.account-mail{position:absolute;left:82px;top:26px;font-size:13.5px;color:#555}
.chev{position:absolute;left:280px;top:31px}
.provider{position:absolute;left:321px;top:17px;font-size:13px;font-weight:500;color:var(--blue)}
.legal{position:absolute;left:0;width:100%;top:438px;text-align:center;font-size:13px;line-height:18px;color:var(--ink-soft)}
.legal a{color:var(--link);text-decoration:none}

/* ---------- vault screen ---------- */
.vault{top:605px;height:539px}
.nav{position:absolute;top:15px;left:0;font-size:8.6px;color:#333}
.nav span{position:absolute;white-space:nowrap}
.search{position:absolute;left:386px;top:7px;width:193px;height:28px;background:#f7f7f7;border:1px solid #eee;border-radius:3px}
.search span{position:absolute;left:12px;top:8px;font-size:8.6px;color:#444}
.search-btn{position:absolute;right:1px;top:1px;width:27px;height:24px;background:var(--blue);border-radius:2px}
.search-btn svg{position:absolute;left:8px;top:7px}
.round-btn{position:absolute;top:11px;width:21px;height:21px;border-radius:50%;background:var(--blue)}
.round-btn svg{position:absolute;left:5px;top:5px}
.rail{position:absolute;left:0;top:42px;width:88px;height:497px;background:var(--white)}
.rail-item{position:absolute;left:0;width:88px;text-align:center;color:#333}
.rail-label{font-size:9.5px;margin-top:2px}
.bluebar{position:absolute;left:88px;top:43px;width:590px;height:27px;background:var(--blue);color:#fff;font-size:8.6px;font-weight:500}
.bluebar span{position:absolute;top:8px}
.cats{position:absolute;left:88px;top:70px;width:157px;height:469px;background:var(--panel)}
.cat{position:absolute;left:16px;height:14px;display:flex;align-items:center;gap:8px;font-size:8.5px;color:#2b2b2b;white-space:nowrap}
.cat .ic{width:10px;height:10px;display:flex;align-items:center;justify-content:center;font-weight:700;font-size:10px;color:#333}
.grid{position:absolute;left:245px;top:71px;width:433px;display:grid;grid-template-columns:141px 156px 136px;grid-template-rows:31px 36px 35px 36px 36px;background:var(--line);gap:1px 1px}
.cell{background:var(--white);display:flex;align-items:center;font-size:8.6px;color:#222;white-space:nowrap}
.cell .ic{margin-right:8px;display:flex}
.c1{padding-left:29px}.c2{padding-left:10px}.c3{padding-left:25px}
</style>
</head>
<body>

<!-- Sign-in screen -->
<section class="screen signin">
  <header class="topbar">
    <div class="brand"><span class="brand-mark"></span>Lumen Keyvault</div>
  </header>
  <h1 class="welcome">Welcome</h1>
  <p class="intro">You can sign in or register from the button below.<br>Please keep in mind how our system works.</p>

  <article class="info-card files">
    <div class="info-icon">
      <svg width="42" height="42" viewBox="0 0 42 42">
        <path d="M9 16v-5a8 8 0 0 1 16 0v2h-5v-2a3 3 0 0 0-6 0v5z" fill="var(--blue)"/>
        <rect x="3" y="16" width="28" height="22" rx="3" fill="var(--blue)"/>
        <circle cx="17" cy="25" r="3.2" fill="#fff"/><rect x="15.8" y="26" width="2.4" height="6" rx="1" fill="#fff"/>
        <path d="M34 14l5-3M35 19h6M34 24l5 3" stroke="var(--blue)" stroke-width="2" stroke-linecap="round"/>
      </svg>
    </div>
    <p class="info-text">Your Files are encrypted with different keys.They are dynamically aggregated only in your browser. we do not store your encryption / Decryption keys.</p>
  </article>

  <article class="info-card drive">
    <div class="info-icon">
      <svg width="36" height="42" viewBox="0 0 36 42">
        <path d="M4 1h19l10 10v28a2 2 0 0 1-2 2H4a2 2 0 0 1-2-2V3a2 2 0 0 1 2-2z" fill="var(--blue)"/>
        <path d="M23 1v10h10" fill="#9ab4e6"/>
        <path d="M9 20h17M9 26h17M9 32h11" stroke="#fff" stroke-width="2.4" stroke-linecap="round"/>
      </svg>
    </div>
    <p class="info-text">your passwords are stored only<br>on one place -your Orbix Folder<br>We do not store anything.</p>
  </article>

  <div class="pager"><span></span><span class="on"></span><span></span></div>

  <div class="account">
    <div class="avatar">H</div>
    <div class="account-name">Sign in as Hana</div>
    <div class="account-mail">hana.team@lumenkeyvault.com</div>
    <svg class="chev" width="9" height="6" viewBox="0 0 9 6"><path d="M1 1l3.5 3.5L8 1" fill="none" stroke="#555" stroke-width="1.2"/></svg>
    <div class="provider">Orbix</div>
  </div>

  <p class="legal">By clicking "Continue Orbix", you agree with our <a href="#">terms of use</a> Leam what data we collect and how<br>we handle it In our <a href="#">Privacy Policy.</a></p>
</section>

<!-- Vault screen -->
<section class="screen vault">
  <header class="topbar">
    <div class="brand" style="top:14px"><span class="brand-mark"></span>Lumen Keyvault</div>
    <nav class="nav">
      <span style="left:155px">Last Used</span>
      <span style="left:203px">Teams</span>
      <span style="left:239px">Password generator</span>
      <span style="left:325px">Overview</span>
    </nav>
    <div class="search"><span>Search</span>
      <div class="search-btn"><svg width="10" height="10" viewBox="0 0 10 10"><circle cx="4" cy="4" r="3" fill="none" stroke="#fff" stroke-width="1.5"/><path d="M6.3 6.3L9 9" stroke="#fff" stroke-width="1.6"/></svg></div>
    </div>
    <div class="round-btn" style="left:596px"><svg width="11" height="11" viewBox="0 0 11 11"><path d="M5.5 1a3 3 0 0 1 3 3v3l1 1.5h-8L2.5 7V4a3 3 0 0 1 3-3z" fill="#fff"/><circle cx="5.5" cy="10" r="1" fill="#fff"/></svg></div>
    <div class="round-btn" style="left:620px"><svg width="11" height="11" viewBox="0 0 11 11"><circle cx="5.5" cy="3.2" r="2.3" fill="#fff"/><path d="M1.5 10.5a4 4 0 0 1 8 0z" fill="#fff"/></svg></div>
    <div class="round-btn" style="left:644px"><svg width="11" height="11" viewBox="0 0 11 11"><ellipse cx="4.5" cy="4.5" rx="4" ry="3" fill="#fff"/><ellipse cx="7" cy="6.5" rx="3.5" ry="2.7" fill="#fff" stroke="var(--blue)" stroke-width=".7"/></svg></div>
  </header>

  <aside class="rail">
    <div class="rail-item" style="top:21px">
      <svg width="14" height="12" viewBox="0 0 14 12"><path d="M7 0L0 6h2v6h4V8h2v4h4V6h2z" fill="#333"/></svg>
      <div class="rail-label">Vault</div>
    </div>
    <div class="rail-item" style="top:71px"><svg width="17" height="15" viewBox="0 0 17 15"><circle cx="8.5" cy="4" r="3" fill="#333"/><circle cx="3" cy="5" r="2.2" fill="#333"/><circle cx="14" cy="5" r="2.2" fill="#333"/><path d="M3 15a5.5 5.5 0 0 1 11 0z" fill="#333"/><path d="M0 11a3 3 0 0 1 5-2.5L3 11zM17 11a3 3 0 0 0-5-2.5L14 11z" fill="#333"/></svg></div>
    <div class="rail-item" style="top:103px"><svg width="14" height="16" viewBox="0 0 14 16"><path d="M7 0a5 5 0 0 1 5 5v5l2 3H0l2-3V5a5 5 0 0 1 5-5z" fill="#333"/><circle cx="7" cy="14.5" r="1.5" fill="#333"/></svg></div>
    <div class="rail-item" style="top:135px"><svg width="16" height="12" viewBox="0 0 16 12"><g fill="#333"><rect x="0" y="0" width="2.5" height="2"/><rect x="4" y="0" width="12" height="2"/><rect x="0" y="3.3" width="2.5" height="2"/><rect x="4" y="3.3" width="12" height="2"/><rect x="0" y="6.6" width="2.5" height="2"/><rect x="4" y="6.6" width="12" height="2"/><rect x="0" y="10" width="2.5" height="2"/><rect x="4" y="10" width="12" height="2"/></g></svg></div>
  </aside>

  <div class="bluebar">
    <span style="left:57px">Categories</span>
    <span style="left:350px">Last Used</span>
    <svg class="abs" style="left:541px;top:9px" width="9" height="9" viewBox="0 0 10 10"><circle cx="4" cy="4" r="3" fill="none" stroke="#fff" stroke-width="1.6"/><path d="M6.3 6.3L9 9" stroke="#fff" stroke-width="1.8"/></svg>
  </div>

  <nav class="cats">
    <div class="cat" style="top:9px"><span class="ic"><svg width="9" height="8" viewBox="0 0 9 8"><g fill="#333"><rect width="4" height="3.5"/><rect x="5" width="4" height="3.5"/><rect y="4.5" width="4" height="3.5"/><rect x="5" y="4.5" width="4" height="3.5"/></g></svg></span>General</div>
    <div class="cat" style="top:35px"><span class="ic"><svg width="9" height="9" viewBox="0 0 9 9"><rect width="9" height="9" rx="1.5" fill="#333"/><circle cx="6" cy="2.5" r="1" fill="#fff"/><circle cx="3" cy="4.5" r="1" fill="#fff"/><circle cx="6" cy="6.5" r="1" fill="#fff"/><path d="M6 2.5L3 4.5L6 6.5" stroke="#fff" stroke-width=".7" fill="none"/></svg></span>Shared With me</div>
    <div class="cat" style="top:62px"><span class="ic"><svg width="10" height="8" viewBox="0 0 10 8"><rect y="1.5" width="10" height="6.5" rx="1" fill="#333"/><rect x="3.3" y="0" width="3.4" height="2" fill="none" stroke="#333" stroke-width=".9"/></svg></span>Work</div>
    <div class="cat" style="top:87px"><span class="ic"><svg width="11" height="9" viewBox="0 0 11 9"><g fill="#333"><circle cx="5.5" cy="2.2" r="2"/><circle cx="2" cy="3" r="1.4"/><circle cx="9" cy="3" r="1.4"/><path d="M2 9a3.5 3.5 0 0 1 7 0z"/><path d="M0 7a2 2 0 0 1 3-1.5L2 7zM11 7a2 2 0 0 0-3-1.5L9 7z"/></g></svg></span>Social media</div>
    <div class="cat" style="top:114px"><span class="ic"><svg width="10" height="9" viewBox="0 0 10 9"><path d="M0 .5h2l1.2 5h5.3L10 2H3" fill="none" stroke="#333" stroke-width="1.1"/><rect x="2.5" y="1.5" width="7" height="3.5" fill="#333"/><circle cx="3.8" cy="7.7" r=".9" fill="#333"/><circle cx="8" cy="7.7" r=".9" fill="#333"/></svg></span>Shopping</div>
    <div class="cat" style="top:140px"><span class="ic"><svg width="10" height="10" viewBox="0 0 10 10"><path d="M9.5.5L6 4l1 5-1 1-2-4-2 2v1.5L1 10 .5 8.5 0 8l.5-1H2l2-2-4-2 1-1 5 1L9.5.5z" fill="#333"/></svg></span>Travel</div>
    <div class="cat" style="top:167px"><span class="ic">$</span>Banking</div>
    <div class="cat" style="top:192px"><span class="ic"><svg width="10" height="7" viewBox="0 0 10 7"><rect width="10" height="7" rx="1" fill="#333"/><path d="M0 .5L5 4 10 .5" fill="none" stroke="#fff" stroke-width=".8"/></svg></span>Emails</div>
    <div class="cat" style="top:216px"><span class="ic"><svg width="10" height="11" viewBox="0 0 10 11"><path d="M3 10V1M1 3l2-2 2 2M7 1v9M5 8l2 2 2-2" fill="none" stroke="#333" stroke-width="1.1"/></svg></span>importAVaultmint-08.02.23</div>
    <div class="cat" style="top:240px"><span class="ic"><svg width="10" height="11" viewBox="0 0 10 11"><path d="M3 10V1M1 3l2-2 2 2M7 1v9M5 8l2 2 2-2" fill="none" stroke="#333" stroke-width="1.1"/></svg></span>importAVaultmint-08.02.23</div>
    <div class="cat" style="top:264px"><span class="ic"><svg width="10" height="11" viewBox="0 0 10 11"><path d="M3 10V1M1 3l2-2 2 2M7 1v9M5 8l2 2 2-2" fill="none" stroke="#333" stroke-width="1.1"/></svg></span>importAVaultmint-08.02.23</div>
    <div class="cat" style="top:285px"><span class="ic"><svg width="9" height="8" viewBox="0 0 9 8"><g fill="#333"><rect width="2.4" height="2"/><rect x="3.3" width="2.4" height="2"/><rect x="6.6" width="2.4" height="2"/><rect y="3" width="2.4" height="2"/><rect x="3.3" y="3" width="2.4" height="2"/><rect x="6.6" y="3" width="2.4" height="2"/><rect y="6" width="2.4" height="2"/><rect x="3.3" y="6" width="2.4" height="2"/><rect x="6.6" y="6" width="2.4" height="2"/></g></svg></span>General</div>
    <div class="cat" style="top:312px"><span class="ic" style="width:13px"><svg width="13" height="8" viewBox="0 0 13 8"><circle cx="3" cy="5" r="2.5" fill="none" stroke="#333" stroke-width=".9"/><circle cx="10" cy="5" r="2.5" fill="none" stroke="#333" stroke-width=".9"/><path d="M3 5l2.5-3.5h4L10 5M5.5 1.5L7 5" fill="none" stroke="#333" stroke-width=".9"/></svg></span>Test<svg style="margin-left:56px" width="6" height="4" viewBox="0 0 6 4"><path d="M.5.5L3 3 5.5.5" fill="none" stroke="#444" stroke-width=".9"/></svg></div>
    <div class="cat" style="top:338px"><span class="ic"><svg width="10" height="8" viewBox="0 0 10 8"><path d="M0 1a1 1 0 0 1 1-1h3l1 1.3h4a1 1 0 0 1 1 1V7a1 1 0 0 1-1 1H1a1 1 0 0 1-1-1z" fill="#333"/></svg></span>Test 123</div>
    <div class="cat" style="top:363px"><span class="ic">$</span>Test 1213</div>
    <div class="cat" style="top:390px"><span class="ic">$</span>Test 1213</div>
    <div class="cat" style="top:417px"><span class="ic"><svg width="10" height="8" viewBox="0 0 10 8"><path d="M0 1a1 1 0 0 1 1-1h3l1 1.3h4a1 1 0 0 1 1 1V7a1 1 0 0 1-1 1H1a1 1 0 0 1-1-1z" fill="#333"/></svg></span>Test 1213x</div>
  </nav>

  <div class="grid">
    <div class="cell c1"><span class="ic"><svg width="9" height="7" viewBox="0 0 9 7"><rect x=".6" y=".6" width="7.8" height="5.8" fill="none" stroke="#333" stroke-width="1.2"/><rect x=".6" y=".6" width="7.8" height="1.8" fill="#333"/></svg></span>Test 3333</div>
    <div class="cell c2"><span class="ic"><svg width="9" height="7" viewBox="0 0 9 7"><rect x=".6" y=".6" width="7.8" height="5.8" fill="none" stroke="#333" stroke-width="1.2"/><rect x=".6" y=".6" width="7.8" height="1.8" fill="#333"/></svg></span>Test 1231</div>
    <div class="cell c3"><span class="ic"><svg width="9" height="7" viewBox="0 0 9 7"><rect x=".6" y=".6" width="7.8" height="5.8" fill="none" stroke="#333" stroke-width="1.2"/><rect x=".6" y=".6" width="7.8" height="1.8" fill="#333"/></svg></span>Test 666</div>

    <div class="cell c1"><span class="ic"><svg width="9" height="7" viewBox="0 0 9 7"><rect x=".6" y=".6" width="7.8" height="5.8" fill="none" stroke="#333" stroke-width="1.2"/><rect x=".6" y=".6" width="7.8" height="1.8" fill="#333"/></svg></span>Shopnest</div>
    <div class="cell c2"><span class="ic"><svg width="9" height="7" viewBox="0 0 9 7"><rect x=".6" y=".6" width="7.8" height="5.8" fill="none" stroke="#333" stroke-width="1.2"/><rect x=".6" y=".6" width="7.8" height="1.8" fill="#333"/></svg></span>Wikora</div>
    <div class="cell c3"><span class="ic" style="font-weight:700;font-size:11px;width:9px">$</span>Coinvault</div>

    <div class="cell c1"><span class="ic"><svg width="9" height="7" viewBox="0 0 9 7"><rect x=".6" y=".6" width="7.8" height="5.8" fill="none" stroke="#333" stroke-width="1.2"/><rect x=".6" y=".6" width="7.8" height="1.8" fill="#333"/></svg></span>Chirpline</div>
    <div class="cell c2"><span class="ic"><svg width="9" height="7" viewBox="0 0 9 7"><rect x=".6" y=".6" width="7.8" height="5.8" fill="none" stroke="#333" stroke-width="1.2"/><rect x=".6" y=".6" width="7.8" height="1.8" fill="#333"/></svg></span>im@lumenkeyvault.comd123</div>
    <div class="cell c3"><span class="ic"><svg width="9" height="7" viewBox="0 0 9 7"><rect x=".6" y=".6" width="7.8" height="5.8" fill="none" stroke="#333" stroke-width="1.2"/><rect x=".6" y=".6" width="7.8" height="1.8" fill="#333"/></svg></span>Kontra</div>

    <div class="cell c1"><span class="ic"><svg width="9" height="7" viewBox="0 0 9 7"><rect x=".6" y=".6" width="7.8" height="5.8" fill="none" stroke="#333" stroke-width="1.2"/><rect x=".6" y=".6" width="7.8" height="1.8" fill="#333"/></svg></span>Threadly</div>
    <div class="cell c2"><span class="ic"><svg width="9" height="7" viewBox="0 0 9 7"><rect x=".6" y=".6" width="7.8" height="5.8" fill="none" stroke="#333" stroke-width="1.2"/><rect x=".6" y=".6" width="7.8" height="1.8" fill="#333"/></svg></span>Test ccc</div>
    <div class="cell c3"><span class="ic"><svg width="9" height="7" viewBox="0 0 9 7"><rect x=".6" y=".6" width="7.8" height="5.8" fill="none" stroke="#333" stroke-width="1.2"/><rect x=".6" y=".6" width="7.8" height="1.8" fill="#333"/></svg></span>Text</div>

    <div class="cell c1"><span class="ic"><svg width="9" height="7" viewBox="0 0 9 7"><rect x=".6" y=".6" width="7.8" height="5.8" fill="none" stroke="#333" stroke-width="1.2"/><rect x=".6" y=".6" width="7.8" height="1.8" fill="#333"/></svg></span>Filmdex</div>
    <div class="cell c2"><span class="ic"><svg width="9" height="7" viewBox="0 0 9 7"><rect x=".6" y=".6" width="7.8" height="5.8" fill="none" stroke="#333" stroke-width="1.2"/><rect x=".6" y=".6" width="7.8" height="1.8" fill="#333"/></svg></span>Test 1111</div>
    <div class="cell c3"><span class="ic"><svg width="9" height="7" viewBox="0 0 9 7"><rect x=".6" y=".6" width="7.8" height="5.8" fill="none" stroke="#333" stroke-width="1.2"/><rect x=".6" y=".6" width="7.8" height="1.8" fill="#333"/></svg></span>Test 77</div>
  </div>
</section>

</body>
</html>
```